Nootropic Supplement Label Design

Hello everyone! Thanks for looking at our project.

We are need a really cool label design that stands out, but also remains slick and clean. We will of course want finished AI / PDF files for any minor text edits, and to send to print.

Product type: Nootropics. (think skyward tablet from the movie)
Brand Name: Quarvant (logo will be provided)
Product Name: Zelbrinox
Tagline: Quarvantly Fueled Nootropics (to be placed under logo)
Slogan: Go Boundfree

We would like the brand name logo to not be so big, more focus on the name Zelbrinox.

Would like some type of Neuron design, something that cool. This product is going to enhance brain function that is why. This part should be kind of bright / neon looking as we might have it shiny or holographic on the print.

Colors, we are open to anything.

Fonts, we like cool for the name of the product, but professional and clean for the most part.

The bottle will be a normal white bottle that holds capsules. Please provide the design with the bottle as well.

Supplement Facts just put random things on this. We typically like it to be transparent with the background. Instead of a white box with black font.

Buzzwords that you can include:
Enhances:
Mental Focus
Clarity
Memory

PLEASE NOTE ON THE LOGO, THE BLUE QUARVANT SYMBOL COLOR CAN BE CHANGED TO WHAT YOU WANT IT TO BE :D

Have it match whatever color scheme you do. Thank you!

Example of another companies design. https://www.vantocapsulehub.com/image/cache/data/fa/Farreach/418269037452-1-750x750.jpg

We do not want a design like this, just showing example. This is probably considered the coolest one on the market vs other Nootropic products. We want to stand out too. :)

Target Market(s)

18-30 College Millienials

Industry/Entity Type

Nutrition

Font styles to use
Sans Serif

Requirements
Must have
• Logo provided.
Nice to have
• Neruon transmitter type design on the label.
Should not have
• Plain white label.

```html
<!DOCTYPE html>
<html lang="en">
<head>
<meta charset="utf-8">
<title>Zelbrinox Label Concepts</title>
<link rel="stylesheet" href="https://fonts.googleapis.com/css2?family=Advent+Pro:wght@300;400&family=Exo+2:wght@400;500&family=Open+Sans:wght@400;700&display=swap">
<style>
  :root {
    --navy: #1b1f5e;
    --deep: #232a72;
    --cyan: #3ec6f2;
    --sky: #5fd0f5;
    --steel: #7a8aa8;
    --ink: #1a1a1a;
    --frame: #b9bcc4;
    --facts-blue: #2b7fc4;
    --white: #ffffff;
  }
  * { margin: 0; padding: 0; box-sizing: border-box; }
  html, body { width: 1200px; height: 1000px; overflow: hidden; background: var(--white); }
  body { position: relative; font-family: "Open Sans", sans-serif; color: var(--ink); }

  .label {
    position: absolute; width: 850px; height: 347px;
    border: 1px solid var(--frame); overflow: hidden; background: var(--white);
  }
  .label--outline { left: 180px; top: 145px; }
  .label--banner { left: 175px; top: 600px; }

  .label__art { position: absolute; inset: 0; width: 850px; height: 347px; }

  .top-band {
    position: absolute; left: 0; top: 20px; width: 850px; height: 90px;
    background: linear-gradient(90deg, rgba(62,198,242,0) 0%, var(--cyan) 22%, var(--sky) 50%, var(--cyan) 78%, rgba(62,198,242,0) 100%);
  }

  .product-name {
    position: absolute; left: 0; width: 850px; text-align: center;
    font-family: "Advent Pro", sans-serif; font-weight: 300; letter-spacing: 1px;
  }
  .label--outline .product-name {
    top: 20px; font-size: 64px; line-height: 70px; color: var(--deep);
    text-shadow: 0 0 6px rgba(120,110,220,.55), 0 0 14px rgba(140,130,230,.45);
  }
  .label--banner .product-name {
    top: 18px; font-size: 62px; line-height: 68px; color: var(--white);
  }

  .slogan {
    position: absolute; font-family: "Exo 2", sans-serif; font-weight: 500;
    color: var(--white); text-align: center; letter-spacing: 1px;
  }
  .label--outline .slogan {
    left: 260px; top: 222px; width: 300px; height: 18px; line-height: 18px; font-size: 13px;
    background: linear-gradient(90deg, rgba(62,198,242,0), var(--cyan) 25%, var(--cyan) 75%, rgba(62,198,242,0));
  }
  .label--banner .slogan { left: 0; width: 850px; top: 86px; font-size: 14px; }

  .facts {
    position: absolute; width: 132px; height: 130px; border-radius: 10px;
    padding: 7px 8px; font-size: 4.3px; line-height: 6.2px;
  }
  .label--outline .facts { left: 40px; top: 50px; border: 2px solid var(--frame); }
  .label--banner .facts { left: 42px; top: 50px; border: 2px solid var(--facts-blue); }
  .facts__title { font-size: 12px; line-height: 16px; font-weight: 700; margin-bottom: 4px; }
  .label--outline .facts__title { color: var(--steel); }
  .label--banner .facts__title { color: var(--facts-blue); }
  .facts__row { display: flex; justify-content: space-between; border-bottom: .5px solid #999; }
  .facts__row--indent span:first-child { padding-left: 8px; }
  .facts__row--plain { border: none; }
  .facts__gap { height: 8px; }
  .facts__note { margin-top: 3px; }

  .ingredients { position: absolute; left: 58px; top: 186px; font-size: 11px; font-weight: 700; }
  .label--outline .ingredients { color: var(--steel); }
  .label--banner .ingredients { color: var(--facts-blue); left: 58px; top: 186px; }

  .directions { position: absolute; left: 614px; top: 42px; width: 200px; font-size: 9px; line-height: 11.5px; }
  .directions__head { font-weight: 700; font-size: 9.5px; }
  .directions p { margin-bottom: 9px; }

  .brand { position: absolute; left: 612px; top: 178px; width: 186px; text-align: center; }
  .brand__name {
    display: inline-flex; align-items: center; gap: 6px;
    font-family: "Exo 2", sans-serif; font-weight: 400; font-size: 22px; letter-spacing: 1px; color: var(--ink);
  }
  .brand__dot { width: 10px; height: 10px; border-radius: 50%; background: var(--deep); }
  .brand__tagline {
    margin-top: 2px; border-top: .5px solid #999; padding-top: 2px;
    font-family: "Exo 2", sans-serif; font-size: 5px; letter-spacing: .5px; color: var(--ink); text-transform: uppercase;
  }

  .count { position: absolute; left: 0; width: 850px; top: 285px; text-align: center; color: var(--white); font-size: 8px; }
  .claim {
    position: absolute; left: 0; width: 850px; top: 298px; text-align: center;
    font-family: "Exo 2", sans-serif; font-size: 14.5px; line-height: 17px; letter-spacing: 1px;
    color: var(--white); text-transform: uppercase;
  }
</style>
</head>
<body>

<section class="label label--outline">
  <svg class="label__art" viewBox="0 0 850 347" aria-hidden="false">
    <defs>
      <linearGradient id="waveFillA" x1="0" x2="1" y1="0" y2="0">
        <stop offset="0" stop-color="#1b1f5e"/>
        <stop offset=".55" stop-color="#2a4f95"/>
        <stop offset="1" stop-color="#47c8f2"/>
      </linearGradient>
      <radialGradient id="neuronA" cx=".5" cy=".5" r=".5">
        <stop offset="0" stop-color="#dff6ff"/>
        <stop offset=".18" stop-color="#3fa7e0"/>
        <stop offset=".6" stop-color="#2f6fb3" stop-opacity=".55"/>
        <stop offset="1" stop-color="#5fd0f5" stop-opacity="0"/>
      </radialGradient>
    </defs>
    <g role="img" aria-label="Glowing blue neuron illustration with branching dendrites">
      <ellipse cx="410" cy="150" rx="220" ry="150" fill="url(#neuronA)"/>
    </g>
    <path d="M0,258 C200,236 420,262 600,246 C720,236 800,220 850,214 L850,347 L0,347 Z" fill="url(#waveFillA)"/>
    <path d="M0,262 C220,248 430,262 600,252 C720,244 800,232 850,226" fill="none" stroke="#5fd0f5" stroke-width="3" opacity=".8"/>
  </svg>

  <h1 class="product-name">ZELBRINOX</h1>
  <div class="slogan">GO BOUNDFREE</div>

  <div class="facts">
    <div class="facts__title">Supplement Facts</div>
    <div class="facts__row facts__row--plain"><span>Serving Size : 01 Capsule</span></div>
    <div class="facts__row facts__row--plain"><span>Serving Per Container: 90</span><span>% Daily*</span></div>
    <div class="facts__gap"></div>
    <div class="facts__row"><span>Total Fat 2g</span><span>3%</span></div>
    <div class="facts__row facts__row--indent"><span>Saturated Fat 0.5g</span><span>3%</span></div>
    <div class="facts__row facts__row--indent"><span>Polyunsaturated Fat 1g</span><span>0%</span></div>
    <div class="facts__row facts__row--indent"><span>Monounsaturated Fat 1.5g</span><span>0%</span></div>
    <div class="facts__row"><span>Vitamin A 4250 IU</span><span>85%</span></div>
    <div class="facts__row"><span>Vitamin D 425 IU</span><span>100%</span></div>
    <div class="facts__row"><span>Omega-3 fatty acids 0.5g</span><span>0%</span></div>
    <div class="facts__note">* Percent Daily Values are based on a 2,000 calorie diet.</div>
  </div>
  <div class="ingredients">Ingredients:</div>

  <div class="directions">
    <p><span class="directions__head">SUGGESTED USE:</span><br>As a dietary supplement, take<br>1 tablet daily with water.</p>
    <p><span class="directions__head">CAUTION:</span><br>Consult your health care provider<br>prior to use if you are pregnant or<br>nursing, have a medical condition<br>or when taking any medication.<br>Do not exceed suggested usage.</p>
  </div>
  <div class="brand">
    <div class="brand__name"><span class="brand__dot"></span>QUARVANT</div>
    <div class="brand__tagline">Quarvantly Fueled Nootropics</div>
  </div>

  <div class="count">40 capsules</div>
  <div class="claim">Quarvantly<br>Fueled Nootropics</div>
</section>

<section class="label label--banner">
  <div class="top-band"></div>
  <svg class="label__art" viewBox="0 0 850 347">
    <defs>
      <linearGradient id="waveFillB" x1="0" x2="1" y1="0" y2="0">
        <stop offset="0" stop-color="#1b1f5e"/>
        <stop offset=".55" stop-color="#2a4f95"/>
        <stop offset="1" stop-color="#47c8f2"/>
      </linearGradient>
      <radialGradient id="neuronB" cx=".5" cy=".5" r=".5">
        <stop offset="0" stop-color="#e6f8ff"/>
        <stop offset=".16" stop-color="#3fa7e0"/>
        <stop offset=".6" stop-color="#2a5da8" stop-opacity=".6"/>
        <stop offset="1" stop-color="#5fd0f5" stop-opacity="0"/>
      </radialGradient>
    </defs>
    <g role="img" aria-label="Large glowing blue neuron illustration with branching dendrites">
      <ellipse cx="405" cy="170" rx="260" ry="175" fill="url(#neuronB)"/>
    </g>
    <path d="M0,250 C200,232 420,256 600,242 C720,232 800,222 850,216 L850,347 L0,347 Z" fill="url(#waveFillB)"/>
    <path d="M0,256 C220,242 430,256 600,248 C720,240 800,230 850,224" fill="none" stroke="#5fd0f5" stroke-width="3" opacity=".8"/>
  </svg>

  <h1 class="product-name">ZELBRINOX</h1>
  <div class="slogan">GO BOUNDFREE</div>

  <div class="facts">
    <div class="facts__title">Supplement Facts</div>
    <div class="facts__row facts__row--plain"><span>Serving Size : 01 Capsule</span></div>
    <div class="facts__row facts__row--plain"><span>Serving Per Container: 90</span><span>% Daily*</span></div>
    <div class="facts__gap"></div>
    <div class="facts__row"><span>Total Fat 2g</span><span>3%</span></div>
    <div class="facts__row facts__row--indent"><span>Saturated Fat 0.5g</span><span>3%</span></div>
    <div class="facts__row facts__row--indent"><span>Polyunsaturated Fat 1g</span><span>0%</span></div>
    <div class="facts__row facts__row--indent"><span>Monounsaturated Fat 1.5g</span><span>0%</span></div>
    <div class="facts__row"><span>Vitamin A 4250 IU</span><span>85%</span></div>
    <div class="facts__row"><span>Vitamin D 425 IU</span><span>100%</span></div>
    <div class="facts__row"><span>Omega-3 fatty acids 0.5g</span><span>0%</span></div>
    <div class="facts__note">* Percent Daily Values are based on a 2,000 calorie diet.</div>
  </div>
  <div class="ingredients">Ingredients:</div>

  <div class="directions">
    <p><span class="directions__head">SUGGESTED USE:</span><br>As a dietary supplement, take<br>1 tablet daily with water.</p>
    <p><span class="directions__head">CAUTION:</span><br>Consult your health care provider<br>prior to use if you are pregnant or<br>nursing, have a medical condition<br>or when taking any medication.<br>Do not exceed suggested usage.</p>
  </div>
  <div class="brand">
    <div class="brand__name"><span class="brand__dot"></span>QUARVANT</div>
    <div class="brand__tagline">Quarvantly Fueled Nootropics</div>
  </div>

  <div class="count">40 capsules</div>
  <div class="claim">Quarvantly<br>Fueled Nootropics</div>
</section>

</body>
</html>
```